Business Card for By Karel Voss

Looking to have a business card designed for my lifestyle and fitness company. My company offers personal training, online programming and nutrition advice based out of London, United Kingdom.

I'd like to see modern, sleek designs, focusing on black, matte black or matte grey. Design doesn't need to be overly descriptive as this will also be used as a personal business card. I've included my logo.

Please note that my company is no longer called "By Karel Voss" but instead "By Karel Voss", this is because of my other ventures. Therefore please don't use the "fitness by karel voss" text.

information about my company can be found at www.bykarelvoss.com

Company is also based out of London (United Kingdom) & Sydney (Australia) this could be reflected on the card.

Industry/Entity Type

Business

Contact Information for Business Card

Karel Voss
+44 7382 615027
karel@bykarelvoss.com
www.bykarelvoss.com

Font styles to use
Sans Serif

Requirements
Must have
• All contact details and inclusion of my logo.

```html
<!DOCTYPE html>
<html lang="en">
<head>
<meta charset="utf-8">
<title>By Karel Voss – Business Card</title>
<link rel="stylesheet" href="https://fonts.googleapis.com/css2?family=Exo+2:wght@400;700&display=swap">
<style>
  :root {
    --backdrop: #a9bdb8;
    --card-white: #ffffff;
    --card-black: #231f20;
    --ink: #231f20;
    --ink-soft: #3a3a3a;
    --rule: #9a9a9a;
  }
  * { box-sizing: border-box; margin: 0; padding: 0; }
  html, body {
    width: 1200px;
    height: 1029px;
    overflow: hidden;
    background: var(--backdrop);
    font-family: "Exo 2", sans-serif;
    color: var(--ink);
  }
  .sheet {
    width: 1200px;
    height: 1029px;
    display: flex;
    flex-direction: column;
    align-items: center;
    justify-content: center;
    gap: 70px;
  }
  .card {
    width: 630px;
    height: 360px;
    box-shadow: 0 10px 30px rgba(0, 0, 0, 0.18);
  }
  .card--front {
    background: var(--card-white);
    display: flex;
    align-items: center;
    position: relative;
  }
  .card__brand {
    width: 290px;
    display: flex;
    flex-direction: column;
    align-items: center;
    gap: 14px;
  }
  .brand-mark {
    width: 40px;
    height: 40px;
    background: var(--ink);
  }
  .brand-name {
    font-weight: 700;
    font-size: 26px;
    letter-spacing: 1px;
    text-transform: uppercase;
    color: var(--ink);
  }
  .card__divider {
    width: 1px;
    height: 210px;
    background: var(--rule);
  }
  .card__contact {
    padding-left: 56px;
  }
  .contact-name {
    font-size: 20px;
    font-weight: 400;
    margin-bottom: 26px;
  }
  .contact-list {
    list-style: none;
    display: flex;
    flex-direction: column;
    gap: 10px;
  }
  .contact-list li {
    display: flex;
    align-items: center;
    gap: 12px;
    font-size: 14px;
    color: var(--ink-soft);
  }
  .contact-icon {
    width: 16px;
    height: 16px;
    flex: none;
  }
  .card--back {
    background: var(--card-black);
    display: flex;
    flex-direction: column;
    align-items: center;
    justify-content: center;
    gap: 18px;
  }
  .card--back .brand-mark {
    width: 56px;
    height: 56px;
    background: var(--card-white);
  }
  .card--back .brand-name {
    color: var(--card-white);
    font-size: 34px;
  }
</style>
</head>
<body>
<main class="sheet">
  <section class="card card--front" aria-label="Business card front">
    <div class="card__brand">
      <span class="brand-mark" aria-hidden="true"></span>
      <span class="brand-name">By Karel Voss</span>
    </div>
    <div class="card__divider"></div>
    <div class="card__contact">
      <p class="contact-name">Karel Voss</p>
      <ul class="contact-list">
        <li>
          <svg class="contact-icon" viewBox="0 0 16 16" aria-hidden="true">
            <rect width="16" height="16" rx="2" fill="#231f20"/>
            <rect x="5" y="3" width="6" height="10" rx="1" fill="none" stroke="#fff" stroke-width="1.2"/>
            <circle cx="8" cy="11.3" r="0.7" fill="#fff"/>
          </svg>
          +44 7382 615027
        </li>
        <li>
          <svg class="contact-icon" viewBox="0 0 16 16" aria-hidden="true">
            <rect width="16" height="16" rx="2" fill="#231f20"/>
            <rect x="3" y="4.5" width="10" height="7" fill="none" stroke="#fff" stroke-width="1.2"/>
            <path d="M3 4.5 L8 8.5 L13 4.5" fill="none" stroke="#fff" stroke-width="1.2"/>
          </svg>
          karel@bykarelvoss.com
        </li>
        <li>
          <svg class="contact-icon" viewBox="0 0 16 16" aria-hidden="true">
            <rect width="16" height="16" rx="2" fill="#231f20"/>
            <circle cx="8" cy="8" r="4.5" fill="none" stroke="#fff" stroke-width="1.2"/>
            <path d="M3.5 8 H12.5 M8 3.5 C6 6 6 10 8 12.5 M8 3.5 C10 6 10 10 8 12.5" fill="none" stroke="#fff" stroke-width="1"/>
          </svg>
          www.bykarelvoss.com
        </li>
      </ul>
    </div>
  </section>

  <section class="card card--back" aria-label="Business card back">
    <span class="brand-mark" aria-hidden="true"></span>
    <span class="brand-name">By Karel Voss</span>
  </section>
</main>
</body>
</html>
```